Marou Cay Lodge Christmas wishes 2013

We require postcards designed to mail our to our clients for Christmas. We are a SURF travel company, with a high end market and like to mail our Christmas postcards to all our guests that have stayed with us through the year. Front cover will have images and text (ie Seasons Greeting) and our logo. The back will have space for TO: name & address and postage stamp. Will also have some basic text (ie The Management & Staff at Marou Cay Lodge wish you and your family all the best for the Festive Season and New Year. We look forward to seeing you back at Marou Cay Lodge again soon etc etc). Here is link to main image https://www.filevault-example.com/sh/qwmzrtpx318kle/Zr8pWnQvcB

Target Market(s)

Our clients are mostly mature men (40-70) surfers who purchase luxury surf trips

Industry/Entity Type

Travel

Requirements
Must have
• Ocean Image (front)
Logo x 2 in same colour - Halcyra & Marou Cay Lodge (front)
Text (front)
Back to be white
Space for name & address (back)
Space for postage stamp (back)
Message (back)
Website www.halcyralodges-example.com (back)

```html
<!DOCTYPE html>
<html lang="en">
<head>
<meta charset="utf-8">
<title>Marou Cay Lodge – Seasons Greetings Postcard</title>
<link rel="stylesheet" href="https://fonts.googleapis.com/css2?family=Great+Vibes&family=Tinos:ital,wght@0,400;0,700;1,400;1,700&display=swap">
<style>
  :root {
    --stage: #050505;
    --card-white: #ffffff;
    --sky-deep: #0b2580;
    --sky-mid: #13349a;
    --sea-turquoise: #35c4cf;
    --sea-light: #7fe0dc;
    --sand: #e9ece6;
    --ink: #111111;
    --script-blue: #1f3f9a;
    --rule-grey: #9a9a9a;
    --logo-box: #0b0b0b;
  }
  * { margin: 0; padding: 0; box-sizing: border-box; }
  html, body { width: 928px; height: 1200px; overflow: hidden; background: var(--stage); }
  .canvas { position: relative; width: 928px; height: 1200px; }

  .postcard {
    position: absolute; left: 74px; width: 780px; height: 520px;
    background: var(--card-white);
  }
  .postcard--front { top: 60px; padding: 10px; }
  .postcard--back { top: 620px; }

  /* Front */
  .front-image {
    position: relative; width: 100%; height: 100%;
    background: linear-gradient(180deg, var(--sky-deep) 0%, var(--sky-mid) 52%, #2a6a8a 62%, var(--sand) 70%, var(--sea-turquoise) 78%, var(--sea-light) 100%);
    overflow: hidden;
  }
  .front-title {
    position: absolute; top: 70px; left: 0; right: 0; text-align: center;
    font-family: "Great Vibes", cursive; color: var(--card-white);
    font-size: 92px; line-height: 0.82;
  }
  .front-title span { display: block; }
  .front-title .line-two { padding-left: 70px; }

  .partner-mark {
    position: absolute; left: 40px; bottom: 32px;
    background: var(--logo-box); color: var(--card-white);
    font-family: "Tinos", serif; font-size: 13px; letter-spacing: 2px;
    padding: 8px 16px; text-transform: uppercase;
  }
  .lodge-mark {
    position: absolute; right: 36px; bottom: 120px; text-align: right;
    color: var(--card-white); font-family: "Tinos", serif;
  }
  .lodge-mark__name { display: flex; align-items: center; gap: 8px; justify-content: flex-end; font-size: 17px; }
  .lodge-mark__dot { width: 14px; height: 14px; border-radius: 50%; background: var(--card-white); }
  .lodge-mark__web { font-size: 12px; margin-top: 3px; }

  /* Back */
  .message {
    position: absolute; left: 40px; top: 110px; width: 330px; text-align: center;
    font-family: "Tinos", serif; color: var(--ink); font-size: 16px; line-height: 1.55;
  }
  .message .lodge-name { font-weight: 700; font-style: italic; font-size: 19px; }
  .message .script { font-family: "Tinos", serif; font-style: italic; color: var(--script-blue); font-size: 30px; line-height: 1.2; display: block; }
  .divider { position: absolute; left: 410px; top: 60px; width: 1px; height: 400px; background: var(--rule-grey); }
  .stamp-box {
    position: absolute; right: 40px; top: 36px; width: 86px; height: 100px;
    border: 1px solid var(--rule-grey);
    font-family: "Arial", sans-serif; color: #8a8a8a; font-size: 14px; line-height: 1.25;
    padding: 12px 10px;
  }
  .address-line { position: absolute; left: 450px; width: 290px; height: 1px; background: var(--rule-grey); }
  .website {
    position: absolute; left: 40px; bottom: 28px;
    font-family: "Tinos", serif; font-size: 13px; color: var(--ink);
  }
</style>
</head>
<body>
<main class="canvas">
  <section class="postcard postcard--front">
    <div class="front-image" role="img" aria-label="Photograph of a small tropical island with green trees and white sand beach under a deep blue sky, surrounded by turquoise sea">
      <h1 class="front-title"><span>Seasons</span><span class="line-two">Greetings</span></h1>
      <div class="lodge-mark">
        <div class="lodge-mark__name"><span class="lodge-mark__dot"></span>Marou Cay Lodge</div>
        <div class="lodge-mark__web">maroucaylodge-example.com</div>
      </div>
      <div class="partner-mark">Halcyra Lodges &amp; Resorts</div>
    </div>
  </section>

  <section class="postcard postcard--back">
    <p class="message">
      The Management &amp; Staff at<br>
      <span class="lodge-name">Marou Cay Lodge</span> joins in sending<br>
      you and your family
      <span class="script">Seasons Greetings</span>
      and Good Wishes for the
      <span class="script">New Year.</span>
    </p>
    <div class="divider"></div>
    <div class="stamp-box">Place<br>Stamp<br>Here</div>
    <div class="address-line" style="top:250px"></div>
    <div class="address-line" style="top:310px"></div>
    <div class="address-line" style="top:370px"></div>
    <p class="website">www.halcyralodges-example.com</p>
  </section>
</main>
</body>
</html>
```